Borealis Fuel Industry Expo

I need to have a banner made up for a tradeshow booth backdrop. I don't want there to be any hiring information. This is to promote to other organizations who we are as a remote medical company. We provide medical support to remote camps and vessels. We employ EMT's, Paramedics, Physician Assistants, Off-site Medical Doctor. Our website is corvanimed.com

```html
<!DOCTYPE html>
<html lang="en">
<head>
<meta charset="utf-8">
<title>Corvani Medical – Tradeshow Backdrop</title>
<link rel="stylesheet" href="https://fonts.googleapis.com/css2?family=Montserrat:wght@600;700;800;900&display=swap">
<style>
  :root {
    --navy: #0b0a8c;
    --plum: #6a0a4c;
    --red: #cc0a1c;
    --red-dark: #a8081a;
    --white: #ffffff;
    --sea-light: #8a93a8;
    --sea-dark: #4a5266;
    --page: #e6e6e6;
  }
  * { margin: 0; padding: 0; box-sizing: border-box; }
  html, body {
    width: 1137px;
    height: 1200px;
    overflow: hidden;
    background: var(--page);
    font-family: "Montserrat", sans-serif;
  }
  .backdrop {
    position: absolute;
    left: 20px;
    top: 326px;
    width: 1097px;
    height: 548px;
    overflow: hidden;
    background: var(--white);
    box-shadow: 0 18px 30px rgba(0,0,0,0.18);
  }
  .backdrop-shapes {
    position: absolute;
    inset: 0;
  }
  .brand {
    position: absolute;
    left: 62px;
    top: 38px;
    display: flex;
    align-items: center;
    gap: 18px;
  }
  .brand-dot {
    width: 110px;
    height: 110px;
    border-radius: 50%;
    background: var(--red);
  }
  .brand-name {
    font-weight: 800;
    font-size: 74px;
    letter-spacing: -1px;
    color: var(--navy);
    line-height: 1;
  }
  .headline {
    position: absolute;
    left: 60px;
    top: 190px;
    color: var(--white);
    font-weight: 900;
    font-size: 84px;
    line-height: 89px;
    letter-spacing: -3px;
    text-transform: uppercase;
  }
  .website {
    position: absolute;
    left: 62px;
    top: 490px;
    color: var(--white);
    font-weight: 700;
    font-size: 29px;
    letter-spacing: 7px;
  }
  .phone {
    position: absolute;
    left: 735px;
    top: 45px;
    width: 362px;
    height: 56px;
    border-radius: 28px 0 0 28px;
    background: var(--red);
    color: var(--white);
    font-weight: 800;
    font-size: 37px;
    line-height: 56px;
    padding-left: 26px;
    letter-spacing: -0.5px;
  }
  .services-title {
    position: absolute;
    left: 772px;
    top: 333px;
    width: 200px;
    text-align: center;
    color: var(--white);
    font-weight: 800;
    font-size: 22px;
  }
  .service {
    position: absolute;
    display: flex;
    align-items: center;
    gap: 14px;
    color: var(--white);
    font-weight: 700;
    font-size: 15px;
    line-height: 21px;
  }
  .service-icon {
    width: 58px;
    height: 58px;
    border-radius: 50%;
    background: var(--red);
    border: 3px solid var(--white);
    display: flex;
    align-items: center;
    justify-content: center;
    flex-shrink: 0;
  }
  .service-icon svg { width: 32px; height: 32px; }
  .service--emt { left: 696px; top: 375px; }
  .service--paramedic { left: 872px; top: 375px; }
  .service--pa { left: 696px; top: 451px; }
  .service--doctor { left: 872px; top: 451px; }
</style>
</head>
<body>
  <main class="backdrop">
    <svg class="backdrop-shapes" width="1097" height="548" viewBox="0 0 1097 548">
      <defs>
        <linearGradient id="band-gradient" x1="0" y1="0" x2="1" y2="0">
          <stop offset="0" stop-color="var(--navy)"/>
          <stop offset="0.35" stop-color="var(--navy)"/>
          <stop offset="1" stop-color="var(--plum)"/>
        </linearGradient>
        <linearGradient id="ring-gradient" x1="0" y1="0" x2="0" y2="1">
          <stop offset="0.15" stop-color="var(--red)"/>
          <stop offset="0.55" stop-color="var(--plum)"/>
          <stop offset="0.85" stop-color="var(--navy)"/>
        </linearGradient>
        <linearGradient id="sea-gradient" x1="0" y1="0" x2="0" y2="1">
          <stop offset="0" stop-color="var(--sea-light)"/>
          <stop offset="1" stop-color="var(--sea-dark)"/>
        </linearGradient>
      </defs>
      <rect class="headline-band" x="0" y="156" width="1097" height="320" fill="url(#band-gradient)"/>
      <rect class="website-band" x="0" y="475" width="1097" height="73" fill="var(--red)"/>
      <circle class="ring-gap" cx="942" cy="270" r="394" fill="var(--white)"/>
      <circle class="ring-accent" cx="942" cy="270" r="384" fill="url(#ring-gradient)"/>
      <circle class="ring-inner" cx="942" cy="270" r="364" fill="var(--white)"/>
      <circle class="photo-area" cx="942" cy="270" r="356" fill="url(#sea-gradient)"
              role="img" aria-label="Photo of a floatplane taking off from open water"/>
    </svg>

    <div class="brand">
      <div class="brand-dot"></div>
      <div class="brand-name">CORVANI</div>
    </div>

    <h1 class="headline">No place<br>is safer<br>than us!</h1>

    <div class="website">www.corvanimed.com</div>

    <div class="phone">(907) 555-0142</div>

    <h2 class="services-title">WE EMPLOY</h2>

    <div class="service service--emt">
      <span class="service-icon">
        <svg viewBox="0 0 32 32" fill="none" stroke="#fff" stroke-width="1.8" stroke-linejoin="round">
          <path d="M3 22V10h15v12M18 14h6l5 5v3h-26"/>
          <circle cx="9" cy="23.5" r="2.5"/><circle cx="23" cy="23.5" r="2.5"/>
          <path d="M10.5 12.5v6M7.5 15.5h6"/>
        </svg>
      </span>
      <span>EMT's</span>
    </div>

    <div class="service service--paramedic">
      <span class="service-icon">
        <svg viewBox="0 0 32 32" fill="none" stroke="#fff" stroke-width="1.8" stroke-linejoin="round">
          <path d="M12 4h8v8h8v8h-8v8h-8v-8H4v-8h8z"/>
        </svg>
      </span>
      <span>Paramedics</span>
    </div>

    <div class="service service--pa">
      <span class="service-icon">
        <svg viewBox="0 0 32 32" fill="none" stroke="#fff" stroke-width="1.8" stroke-linejoin="round">
          <rect x="7" y="6" width="18" height="22" rx="2"/>
          <path d="M12 4h8v4h-8zM11 14h10M11 19h10M11 24h6"/>
        </svg>
      </span>
      <span>Physician<br>Assistants</span>
    </div>

    <div class="service service--doctor">
      <span class="service-icon">
        <svg viewBox="0 0 32 32" fill="none" stroke="#fff" stroke-width="1.8" stroke-linecap="round">
          <path d="M9 4v8a6 6 0 0 0 12 0V4"/>
          <path d="M15 18v4a6 6 0 0 0 12 0v-3"/>
          <circle cx="27" cy="16" r="2.5"/>
        </svg>
      </span>
      <span>Off-site<br>Medical Doctor</span>
    </div>
  </main>
</body>
</html>
```